Seminar Invitation for Financial Planning Group

I want a flyer that I can mail out to 5000 people (targeted group of seniors with high incomes and that own homes) to invite to a seminar we will be holding on March 9th and March 10th of 2010. It is a FREE educational workshop and we want to have a colorful catchy flyer that we will be mailing out that doesn't look to cheesy or like a get rich quick scheme. We are experienced financial planners that are proposing long term practical solutions.

Dates and Locations:
March 9th, 2010- Halvard Pemsley 5:30 p.m.-7:00 p.m.
March 11th, 2010-Vista Colmera Winery 11:00 a.m. -12:30 p.m.

Speakers:
Harold T. Penwick, ChFC and CLU, focuses on the coordination of insurance, retirement, and estate planning. Hal is a member of the Guild of Monetary Advisory Practitioners.
Dana Molvetti, C.F.A., is V.P. of Investment Research at Ledgerpoint Advisors and is a member of the Tarrowfield Circle of Asset Examiners.

Another Speaker:

Social Security Public Relations Director, TBA

At the bottom, it should read, and in similar font as I am posting now:

Harold T. Penwick is a registered representatie with & securities are offered through Ledgerpoint Advisors, Inc. Member FINRA/SIPC CA Insurance License # 0817265 (03-2010)

The font size should be around 12 point

Also, we now have the same of the Social Security Speaker( to go Under Harold T. Penwick and Dana Molvetti),

Marisol Ketter, San Diego Social Security Public Affairs Specialist

Also, please incorporate at the bottom(the first line and phone number/email should be large compared to the rest of the text so it is easy to locate contact info:

To register, please call (555) 273-9614 or email tessa@penwickdale-mail.test.

Due to limited capacity, we reserve the right to refuse unregistered guests. Complimentary parking is provided.

CORRECT DATES AND LOCATIONS ARE:
3/9/10 5:30-7:00PM HALVARD PEMSLEY
3/10/10 11:00-12:30 P.M. VISTA COLMERA INN

ALSO ADD, RIGHT ABOVE THE LONG TERM CARE LINE IN THE TOPICS TO BE DISCUSSED SECTION, PLEASE ADD "Top 10 Myths About Social Security" No need for quotation marks I just want to distinguish the text here. Also, I have uploaded 2 pics, one of Dana Molvetti and one of Marisol Ketter. I am still waiting on one from Hal Penwick and will post it when I receive it. These are to go to left of their name and short description. 

Target Market(s)

Seniors, People who are about to retire, 55+ in age, primarily those with investable assets of 500k+, those who are concerned with their retirement income and their nest egg.

Industry/Entity Type

Insurance

Requirements
Must have
• An Image(not to make up more than 20% of the flyer). Preferably of a family (elderly couple playing with grandkids, maybe in mid-60''s). Maybe a cartoon of a couple wondering about their financial future since the market tanked and depleted their nest egg.
• -Seminar Dates and Times
• -Must be 1 Page
• -Title of Seminar is "Back to Basics"
• 3 Speakers, each an expert in their field.
• 1)Social Security Speaker 2)Dana Molvetti, CFA, and 3) retirement planning expert, Harold T. Penwick

• Topics to Be Discussed at Seminar:
• Roth Conversion Pitfalls and Opportunities
• Market Outlook 2010/2011
• How to Maximize Your Retirement Income
• Can You Afford to Not Have Long Term Care?
• And many more....
• Should not have
• No bags of money or bullions. We are not out to have people make a lot of money off of us, we are just advertising good solid financial advice

```html
<!DOCTYPE html>
<html lang="en">
<head>
<meta charset="utf-8">
<title>Back to Basics – Seminar Invitation</title>
<link rel="stylesheet" href="https://fonts.googleapis.com/css2?family=Arimo:wght@700&family=PT+Sans&family=Sorts+Mill+Goudy&display=swap">
<style>
  :root {
    --paper: #ffffff;
    --cream: #f3ebe0;
    --green: #236d4c;
    --green-dark: #164a34;
    --green-text: #1f4a2e;
    --olive: #3f5a2b;
    --gold: #f4b300;
    --ink: #000000;
    --body-grey: #3a3a3a;
    --white: #ffffff;
  }
  * { margin: 0; padding: 0; box-sizing: border-box; }
  html, body { width: 930px; height: 1200px; overflow: hidden; background: var(--paper); }
  .flyer { position: relative; width: 930px; height: 1200px; background: var(--paper); overflow: hidden; }
  .backdrop { position: absolute; inset: 0; }
  .seminar-title {
    position: absolute; left: 110px; top: 455px;
    font-family: "PT Sans", sans-serif; font-size: 62px; line-height: 1;
    color: var(--olive); white-space: nowrap;
  }
  .seminar-title .accent { color: var(--gold); }
  .section-heading {
    position: absolute; font-family: "Arimo", Arial, sans-serif; font-weight: 700;
    font-size: 29px; line-height: 1; white-space: nowrap;
  }
  .topics-heading { left: 27px; top: 552px; color: var(--ink); }
  .topic-list {
    position: absolute; left: 26px; top: 603px; list-style: none;
    font-family: "Sorts Mill Goudy", Georgia, serif; font-size: 27px;
    color: var(--green-text); line-height: 44px;
  }
  .topic-list li { position: relative; padding-left: 32px; }
  .topic-list li::before {
    content: ""; position: absolute; left: 2px; top: 15px;
    width: 12px; height: 12px; border-radius: 50%;
    border: 3px solid var(--green);
  }
  .speakers-heading {
    position: absolute; left: 508px; top: 848px;
    font-family: "Arimo", Arial, sans-serif; font-weight: 700;
    font-size: 27px; color: var(--white);
  }
  .speaker-list {
    position: absolute; left: 460px; top: 900px; list-style: none;
    font-family: "Sorts Mill Goudy", Georgia, serif; font-size: 24px;
    line-height: 45px; color: var(--white);
  }
  .dates-heading { left: 24px; top: 1064px; color: var(--green-dark); }
  .date-list {
    position: absolute; left: 24px; top: 1110px; list-style: none;
    font-family: "Sorts Mill Goudy", Georgia, serif; font-size: 19px;
    line-height: 34px; color: var(--body-grey);
  }
</style>
</head>
<body>
<main class="flyer">
  <svg class="backdrop" width="930" height="1200" viewBox="0 0 930 1200" aria-hidden="true">
    <defs>
      <linearGradient id="family-tones" x1="0" y1="0" x2="1" y2="1">
        <stop offset="0" stop-color="#d9b9a3"/>
        <stop offset="0.5" stop-color="#bcd2e0"/>
        <stop offset="1" stop-color="#e6ddd6"/>
      </linearGradient>
    </defs>
    <rect class="cream-field" x="0" y="330" width="918" height="722" fill="var(--cream)"/>
    <rect class="accent-bar" x="652" y="15" width="45" height="332" fill="var(--green-dark)"/>
    <rect class="accent-block" x="697" y="15" width="218" height="332" fill="var(--green)"/>
    <polygon class="speakers-panel" points="430,885 915,885 915,1196 430,1052" fill="var(--green)"/>
    <rect class="speakers-band" x="430" y="840" width="485" height="45" fill="var(--green-dark)"/>
  </svg>

  <svg style="position:absolute;left:0;top:0" width="670" height="460" viewBox="0 0 670 460" role="img" aria-label="Photo of smiling grandparents with their young granddaughter">
    <path d="M0 0 H660 V345 Q340 470 15 352 L0 345 Z" fill="url(#family-tones)"/>
    <path d="M15 352 Q340 470 660 345" fill="none" stroke="var(--green)" stroke-width="6"/>
  </svg>

  <h1 class="seminar-title">"Back to <span class="accent">Basics</span>"</h1>

  <h2 class="section-heading topics-heading">Topics to Be Discussed at Seminar:</h2>
  <ul class="topic-list">
    <li>Roth Conversion Pitfalls and<br>Opportunities</li>
    <li>Market Outlook 2010/2011</li>
    <li>How to Maximize Your Retirement Income</li>
    <li>Can You Afford to Not Have Long Term Care?</li>
    <li>And many more....</li>
  </ul>

  <h2 class="speakers-heading">Speakers</h2>
  <ul class="speaker-list">
    <li>1)Social Security Speaker.</li>
    <li>2)Dana Molvetti. CFA.</li>
    <li>3 Harold T. Penwick, ChFC and CLU</li>
  </ul>

  <h2 class="section-heading dates-heading">Dates and Locations:</h2>
  <ul class="date-list">
    <li>March 9th, 2010- Halvard Pemsley 5:30 p.m.-7:00 p.m.</li>
    <li>March 11th, 2010-Vista Colmera Winery 11:00 a.m. -12:30 p.m.</li>
  </ul>
</main>
</body>
</html>
```